BLUE HAVEN (Business Card for Training Company)

Blue Haven is a training and consultancy company with a focus on executive protection and medical. I would like the card to be nice and sharp, not overdone and in black and red. I would also like it to highlight that it is "A Dravin Company"

I would like it to be simple and highlight a few things.

1. Name
2. Title
3. Phone Number
4. Email

I would also like www.dravinholdings.example/blue-haven to be on the card somewhere.

Target Market(s)

Security Companies

Industry/Entity Type

Security

Contact Information for Business Card

Blue Haven is a training and consultancy company with a focus on executive protection and medical. I would like the card to be nice and sharp, not overdone and in black and red. I would also like it to highlight that it is "A Dravin Company" I would like it to be simple and highlight a few things. 1. Name 2. Title 3. Phone Number 4. Email I would also like www.dravinholdings.example/blue-haven to be on the card somewhere.

Requirements
Must have
• A Dravin Company listed on the card and the website
Nice to have
• Highlight Medical Training, Consultancy & Executive Protection Courses

```html
<!DOCTYPE html>
<html lang="en">
<head>
<meta charset="utf-8">
<title>Blue Haven — Business Card</title>
<link rel="stylesheet" href="https://fonts.googleapis.com/css2?family=Exo+2:wght@800&family=Roboto:wght@400;500&display=swap">
<style>
  :root {
    --backdrop: #2a2a2a;
    --card-black: #000000;
    --card-white: #ffffff;
    --brand-red: #6b0f12;
    --ink: #111111;
    --light: #e6e6e6;
  }
  * { margin: 0; padding: 0; box-sizing: border-box; }
  html, body { width: 1200px; height: 1200px; overflow: hidden; }
  body {
    background: var(--backdrop);
    position: relative;
    font-family: "Roboto", Arial, sans-serif;
  }
  .card {
    position: absolute;
    left: 220px;
    width: 757px;
    height: 432px;
    overflow: hidden;
  }
  .card--front { top: 121px; background: var(--card-black); }
  .card--back { top: 604px; background: var(--card-white); }

  .wordmark {
    font-family: "Exo 2", "Arial Black", sans-serif;
    font-weight: 800;
    text-transform: uppercase;
    line-height: 0.9;
    letter-spacing: 2px;
  }
  .card--front .wordmark {
    position: absolute;
    left: 0; right: 0;
    top: 134px;
    text-align: center;
    font-size: 74px;
    color: var(--light);
  }
  .parent-line {
    position: absolute;
    left: 0; right: 0;
    top: 293px;
    text-align: center;
    color: var(--card-white);
    font-family: "Exo 2", "Arial Black", sans-serif;
    font-weight: 800;
    font-size: 18px;
    letter-spacing: 9px;
    text-transform: uppercase;
  }
  .service-band {
    position: absolute;
    left: 0; right: 0; bottom: 0;
    height: 37px;
    background: var(--brand-red);
    color: var(--card-white);
    font-weight: 500;
    font-size: 17px;
    letter-spacing: 0.3px;
    display: flex;
    align-items: center;
    justify-content: center;
  }

  .card--back .wordmark {
    position: absolute;
    right: 50px;
    top: 46px;
    font-size: 58px;
    color: var(--brand-red);
    text-align: left;
  }
  .person {
    position: absolute;
    left: 44px;
    top: 208px;
  }
  .person__name {
    font-family: "Exo 2", "Arial Black", sans-serif;
    font-weight: 800;
    font-size: 33px;
    color: var(--brand-red);
    line-height: 1;
    text-transform: uppercase;
  }
  .person__title {
    margin-top: 4px;
    font-size: 20px;
    color: var(--ink);
  }
  .contacts {
    position: absolute;
    left: 44px;
    top: 310px;
    list-style: none;
  }
  .contacts li {
    display: flex;
    align-items: center;
    height: 27.5px;
    font-size: 20px;
    color: var(--ink);
  }
  .contacts svg {
    width: 18px; height: 18px;
    margin-right: 10px;
    flex: none;
  }
</style>
</head>
<body>

<section class="card card--front" aria-label="Card front">
  <div class="wordmark">Blue<br>Haven</div>
  <p class="parent-line">A Dravin Company</p>
  <p class="service-band">Medical Training, Consultancy &amp; Executive Protection Courses</p>
</section>

<section class="card card--back" aria-label="Card back">
  <div class="wordmark">Blue<br>Haven</div>

  <div class="person">
    <h1 class="person__name">Marcus Ellery</h1>
    <p class="person__title">Founder &amp; CEO</p>
  </div>

  <ul class="contacts">
    <li>
      <svg viewBox="0 0 24 24" aria-hidden="true"><path fill="var(--brand-red)" d="M6.6 10.8a15.1 15.1 0 0 0 6.6 6.6l2.2-2.2c.3-.3.7-.4 1-.2 1.1.4 2.3.6 3.6.6.6 0 1 .4 1 1V20c0 .6-.4 1-1 1A17 17 0 0 1 3 4c0-.6.4-1 1-1h3.5c.6 0 1 .4 1 1 0 1.3.2 2.5.6 3.6.1.3 0 .7-.2 1z"/><path fill="none" stroke="var(--brand-red)" stroke-width="1.6" d="M14 6.5a4 4 0 0 1 3.5 3.5M14 3a7.5 7.5 0 0 1 7 7"/></svg>
      +44 7700 918364
    </li>
    <li>
      <svg viewBox="0 0 24 24" aria-hidden="true"><rect x="2" y="5" width="20" height="14" fill="var(--brand-red)"/><path d="M4 7l8 6 8-6" fill="none" stroke="#fff" stroke-width="1.8"/></svg>
      m_ellery@bluehaven.example
    </li>
    <li>
      <svg viewBox="0 0 24 24" aria-hidden="true"><g fill="none" stroke="var(--brand-red)" stroke-width="1.8"><circle cx="12" cy="12" r="9"/><ellipse cx="12" cy="12" rx="4" ry="9"/><path d="M3 12h18M5 7h14M5 17h14"/></g></svg>
      dravinholdings.example/blue-haven
    </li>
  </ul>
</section>

</body>
</html>
```